Kindling Haven of Alabama

We are a disaster relief nonprofit organization that provides relief to families children and pets when a disaster strikes multifamily. We need a easy and powerful piece that tells what we do and draws folks into finding out more. So a piece that could be used at tradeshows or speaking engagements
Updates

Be sure to include our social and other contact info. Added Monday, October 16, 2017

Target Market(s)

Potential Donors & Volunteers

Industry/Entity Type

Non-Profit

Font styles to use
Serif

Colors

Designer to choose colors to be used in the design.

Requirements
Must have
• Our logo and trigger photos I am going to rely on your expertise to create something compelling that is simple and powerful
Nice to have
• Moving pull on the heart strings

```html
<!DOCTYPE html>
<html lang="en">
<head>
<meta charset="utf-8">
<title>Kindling Haven of Alabama – Giving Hope</title>
<link href="https://fonts.googleapis.com/css2?family=Bebas+Neue&family=Arimo:wght@400;700&display=swap" rel="stylesheet">
<style>
  :root {
    --ink-bg: #000000;
    --card: #ffffff;
    --brand-blue: #2a6db5;
    --warm-yellow: #fdd583;
    --text-gray: #7b7b7b;
    --panel-gray: #87868a;
    --white: #ffffff;
  }
  * { margin: 0; padding: 0; box-sizing: border-box; }
  html, body { width: 999px; height: 1200px; overflow: hidden; background: var(--ink-bg); }
  body { position: relative; font-family: "Arimo", Arial, sans-serif; color: var(--text-gray); }

  .card { position: absolute; left: 92px; width: 815px; height: 544px; background: var(--card); overflow: hidden; }
  .card--front { top: 46px; }
  .card--back { top: 618px; }

  .abs { position: absolute; }

  /* Front */
  .headline { left: 40px; top: 22px; font-family: "Bebas Neue", "Oswald", sans-serif; font-size: 94px; line-height: 1; color: var(--brand-blue); letter-spacing: 1px; }
  .subhead { left: 44px; top: 109px; font-size: 18px; font-weight: 700; color: var(--text-gray); }
  .brand { left: 40px; top: 168px; width: 220px; font-size: 34px; line-height: 40px; font-weight: 400; color: var(--text-gray); }
  .intro { left: 33px; top: 297px; width: 356px; font-size: 15px; line-height: 19.6px; text-align: justify; }
  .tagline { left: 34px; top: 480px; width: 320px; font-size: 15px; line-height: 19px; color: var(--brand-blue); }

  .frame { position: absolute; background: var(--warm-yellow); }
  .photo { position: absolute; }
  .frame--selfie { left: 284px; top: 109px; width: 159px; height: 160px; }
  .photo--selfie { left: 12px; top: 12px; width: 137px; height: 136px; background: linear-gradient(160deg, #e7c9b0, #c89a78 55%, #7f8e5a); }
  .frame--hero { left: 453px; top: 0; width: 362px; height: 347px; }
  .photo--hero { left: 11px; top: 0; width: 351px; height: 336px; background: linear-gradient(135deg, #7d7a74, #d8cbb4 45%, #f1efe9 70%, #bcc3cf); }
  .frame--fire { left: 399px; top: 276px; width: 232px; height: 231px; }
  .photo--fire { left: 11px; top: 11px; width: 210px; height: 209px; background: linear-gradient(180deg, #3f4a52, #8b5a2b 40%, #e9802a 65%, #6a3a1a); }
  .frame--kids { left: 645px; top: 358px; width: 159px; height: 159px; }
  .photo--kids { left: 11px; top: 11px; width: 137px; height: 137px; background: linear-gradient(135deg, #5a3a2c, #b8874f 50%, #d8b56a); }

  /* Back */
  .list-title { left: 42px; top: 27px; font-size: 22px; font-weight: 700; color: var(--warm-yellow); letter-spacing: 0.3px; }
  .supply-list { left: 43px; top: 66px; width: 484px; list-style: none; font-size: 14.5px; line-height: 18.2px; }
  .supply-list li { position: relative; padding-left: 28px; }
  .supply-list li::before { content: ""; position: absolute; left: 0; top: 6px; width: 5px; height: 5px; border-radius: 50%; background: var(--warm-yellow); }
  .supply-list strong { font-weight: 700; }
  .supply-list p { text-align: justify; }
  .divider { left: 0; top: 446px; width: 363px; height: 3px; background: var(--warm-yellow); }
  .social { left: 48px; top: 461px; font-size: 18px; display: flex; align-items: center; gap: 12px; }
  .social__mark { width: 20px; height: 20px; background: var(--brand-blue); }
  .website { left: 45px; top: 487px; font-size: 18px; }

  .side-panel { left: 540px; top: 0; width: 275px; height: 544px; background: var(--panel-gray); }
  .side-text { left: 22px; top: 84px; width: 222px; font-size: 14.5px; line-height: 18px; font-weight: 700; color: var(--white); text-align: justify; }
  .frame--team { left: 17px; top: 258px; width: 232px; height: 232px; }
  .photo--team { left: 10px; top: 10px; width: 212px; height: 212px; background: linear-gradient(180deg, #efe8df 0%, #d9cbb9 45%, #4a4548 75%, #2d2b30); }
</style>
</head>
<body>

<section class="card card--front">
  <h1 class="abs headline">Giving Hope</h1>
  <p class="abs subhead">When Disaster Strikes</p>
  <p class="abs brand">Kindling Haven of Alabama</p>
  <p class="abs intro">Kindling Haven of Alabama was Co-Founded by Dara Mills-Whitcomb and her son Tyler Whitcomb to offer support to Residents that have been displaced from Apartment Homes due to fire or other disasters. Often times, displaced residents are placed in vacant apartment homes or even find themselves on the floor of the clubhouse until a plan is devised for next steps.</p>
  <p class="abs tagline">Alabama based 501c3 Nonprofit Disaster Relief Oraganization</p>

  <div class="frame frame--hero"><div class="photo photo--hero" role="img" aria-label="Young co-founder smiling with a teddy bear and boxed relief kits in a car trunk"></div></div>
  <div class="frame frame--selfie"><div class="photo photo--selfie" role="img" aria-label="Co-founders, mother and son, posing outdoors"></div></div>
  <div class="frame frame--fire"><div class="photo photo--fire" role="img" aria-label="Apartment building engulfed in fire"></div></div>
  <div class="frame frame--kids"><div class="photo photo--kids" role="img" aria-label="Children holding teddy bears from relief kits"></div></div>
</section>

<section class="card card--back">
  <h2 class="abs list-title">DISASTER RELIEF KIT SUPPLY LIST</h2>
  <ul class="abs supply-list">
    <li><strong>Twin Air Mattress (8.00 at Bargain Barn)</strong>
      <p>On almost all occasions, property management will place a resident into a vacant apartment. Our disaster relief kits give them everything that victims of disaster need to take refuge for the first few nights. Most often our kits are all that these families have.</p></li>
    <li><strong>Standard Pillows (2.37 at Bargain Barn)</strong></li>
    <li><strong>Air Pumps (13.00 Bargain Barn)</strong></li>
    <li><strong>Blankets/Throws (2.88 at Bargain Barn)</strong>
      <p>Small rolled fleece throws. We also take handmade items/must be new</p></li>
    <li><strong>Towels/Washcloths/Flat Sheets</strong></li>
    <li><strong>Flip Flops- Solid Colors-All sizes (Bargain Barn $1)</strong>
      <p>Most often victims of disaster are not wearing shoes due to the rushed escape, etc. We provide them with flip flops on scene</p></li>
    <li><strong>Penny Shelf Items All $1</strong>
      <p>Brush/Comb Combo, Toothbrush/Paste Travel Combo, Wipes, Deodorant, Hand Sanitizer, Soap, Shampoo, Conditioner<br>We prefer travel sized to ensure that it fits into our boxes and does not leak.</p></li>
    <li><strong>Cases of Bottled Water</strong></li>
  </ul>
  <div class="abs divider"></div>
  <div class="abs social"><span class="social__mark"></span><span>KindlingHaven</span></div>
  <p class="abs website">Kindlinghavenofalabama.org</p>

  <aside class="abs side-panel">
    <p class="abs side-text">Kindling Haven of Alabama is a Birmingham, Alabama based 501c3 nonprofit organization that provides disaster relief to Residents displaced from Apartment Homes across the state of Alabama.</p>
    <div class="frame frame--team"><div class="photo photo--team" role="img" aria-label="Volunteer team standing together indoors"></div></div>
  </aside>
</section>

</body>
</html>
```